Business Card

I need a business card for my work as an energy lawyer. I am a single prctioner and I consult to energy companies regarding a variety of legal issues involving environmental matters, energy efficiency, regulations and contractual arrangements. i need a distinctive business card that stands out and is easy to read. I like bold colors or high contrast. I like a sparse architectural design. The font should be easy to read (many of my clients use reading glasses and are concerned about small type). The card should communicate that I am somewhat different from ordinary legal counsel. Below are some examples of cards that I like. Thank you for your interest and thought. Glen Dusty Harlow
Updates

Thanks to everyone who has submitted a design.  My general comments are:

1.  I like the colourful cards and the high contrast cards.
2.  I prefer the use of icons for home address, phone, mobile and email.
3.  For the high contrast cards please use three colours - black background, and red and white for the logo or information.
4.  The mobile number area code should be 403 and not 404.
5.  I also need to add a direct phone line which is 555-318-2967.

Thank you,

Glen Harlow

Project Deadline Extended
Reason: I have briefly extended the deadline by three days to allow those individuals who responded early to revise their designs based upon the subsequent clarification of the colours (red, white, black background) and the request to use icons and add a direct phone number.

Industry/Entity Type

Business

```html
<!DOCTYPE html>
<html lang="en">
<head>
<meta charset="utf-8">
<title>Glen Dusty Harlow — Business Card</title>
<link href="https://fonts.googleapis.com/css2?family=Arimo:wght@400;700&display=swap" rel="stylesheet">
<style>
  :root {
    --paper: #d9d9d7;
    --card: #0b0b0b;
    --red: #e0262b;
    --white: #f2f2f2;
    --grey: #bdbdbd;
    --font: "Arimo", Arial, sans-serif;
  }
  * { margin: 0; padding: 0; box-sizing: border-box; }
  html, body {
    width: 1200px; height: 1200px; overflow: hidden;
    background: var(--paper);
    font-family: var(--font);
  }
  .card {
    position: absolute;
    left: 150px;
    width: 900px; height: 514px;
    background: var(--card);
    box-shadow: 0 6px 18px rgba(0,0,0,.18);
  }
  .card--back { top: 44px; }
  .card--front { top: 642px; }

  /* Back: contact side */
  .monogram {
    position: absolute; left: 80px; top: 50px;
    color: var(--red); font-weight: 700;
    font-size: 118px; line-height: 1; letter-spacing: 2px;
  }
  .identity { position: absolute; left: 480px; top: 160px; }
  .identity__name {
    color: var(--red); font-weight: 400;
    font-size: 36px; font-variant: small-caps; letter-spacing: .5px;
    line-height: 1.05;
  }
  .identity__title { color: var(--grey); font-size: 21px; margin-top: 4px; }

  .contact-tab {
    position: absolute; left: 0; top: 200px;
    width: 72px; height: 176px;
    background: var(--red);
    display: flex; flex-direction: column; justify-content: space-around;
    align-items: center; padding: 10px 0;
  }
  .contact-tab svg { width: 22px; height: 22px; fill: var(--card); }
  .contact-list {
    position: absolute; left: 100px; top: 206px;
    list-style: none; color: var(--white);
    font-size: 23px; line-height: 41px;
  }
  .address {
    position: absolute; right: 60px; bottom: 72px;
    color: var(--red); font-size: 24px;
  }

  /* Front: logo side */
  .brand {
    position: absolute; inset: 0;
    display: flex; flex-direction: column; align-items: center; justify-content: center;
  }
  .brand__monogram {
    color: var(--red); font-weight: 700;
    font-size: 190px; line-height: .95; letter-spacing: 4px;
  }
  .brand__name {
    color: var(--red); font-size: 44px;
    font-variant: small-caps; letter-spacing: .5px; margin-top: 6px;
  }
</style>
</head>
<body>
  <section class="card card--back">
    <div class="monogram">GDH</div>
    <div class="identity">
      <p class="identity__name">GlenDustyHarlow</p>
      <p class="identity__title">Barrister and Solicitor, LLB, ICD.D</p>
    </div>

    <div class="contact-tab">
      <svg viewBox="0 0 24 24" aria-label="Office phone"><path d="M6.6 10.8a15 15 0 0 0 6.6 6.6l2.2-2.2a1 1 0 0 1 1-.25 11.4 11.4 0 0 0 3.6.6 1 1 0 0 1 1 1V20a1 1 0 0 1-1 1A17 17 0 0 1 3 4a1 1 0 0 1 1-1h3.5a1 1 0 0 1 1 1c0 1.25.2 2.45.6 3.6a1 1 0 0 1-.25 1z"/></svg>
      <svg viewBox="0 0 24 24" aria-label="Mobile"><path d="M7 1h10a2 2 0 0 1 2 2v18a2 2 0 0 1-2 2H7a2 2 0 0 1-2-2V3a2 2 0 0 1 2-2zm0 3v14h10V4zm5 15.5a1 1 0 1 0 0 2 1 1 0 0 0 0-2z"/></svg>
      <svg viewBox="0 0 24 24" aria-label="Direct line"><path d="M4 3h16v18H4zm3 3v4h10V6zm0 6v2h2v-2zm4 0v2h2v-2zm4 0v2h2v-2zm-8 4v2h2v-2zm4 0v2h2v-2zm4 0v2h2v-2z"/></svg>
      <svg viewBox="0 0 24 24" aria-label="Email"><path d="M2 5h20v14H2zm2 2v.5l8 5 8-5V7zm0 2.9V17h16V9.9l-8 5z"/></svg>
    </div>
    <ul class="contact-list">
      <li>1.555.774.0192</li>
      <li>1.555.560.0384</li>
      <li>555-318-2967</li>
      <li>dusty@dustyharlow.com</li>
    </ul>

    <p class="address">2260 Larch Street S.W., Calgary, Alberta</p>
  </section>

  <section class="card card--front">
    <div class="brand">
      <div class="brand__monogram">GDH</div>
      <p class="brand__name">GlenDustyHarlow</p>
    </div>
  </section>
</body>
</html>
```